Interior designer needs a gorgeous, chic business card design.

A new, small Interior Design firm needs a business card that is chic, contemporary and elegant. Nothing over the top. My interiors are contemporary classic with an elegant feel to them. I like to use quality finishes and products rather than follow the latest fads. Projects can be anything from Pre start selections, bathrooms, kitchens, bedrooms, custom upholstery, furniture, rugs and art etc. The final design should display quality and an achievable sense of chic. I am open to all colours including black but not limited to this.

Business

```html
<!DOCTYPE html>
<html lang="en">
<head>
<meta charset="utf-8">
<title>Liora Interiors – Business Card</title>
<link rel="stylesheet" href="https://fonts.googleapis.com/css2?family=Josefin+Sans:wght@300;600&display=swap">
<style>
  :root {
    --page: #ffffff;
    --sage: #9bbbba;
    --card-white: #ffffff;
    --ink: #111111;
    --reverse: #ffffff;
    --edge: #e6e6e6;
  }
  * { margin: 0; padding: 0; box-sizing: border-box; }
  html, body {
    width: 1200px;
    height: 805px;
    overflow: hidden;
    background: var(--page);
  }
  .canvas {
    position: relative;
    width: 1200px;
    height: 805px;
    font-family: "Josefin Sans", sans-serif;
  }
  .card {
    position: absolute;
  }
  .card--front {
    left: 354px;
    top: 53px;
    width: 483px;
    height: 330px;
    background: var(--sage);
  }
  .card--back {
    left: 372px;
    top: 420px;
    width: 465px;
    height: 331px;
    background: var(--card-white);
    border: 1px solid var(--edge);
  }
  .brand {
    position: absolute;
    font-weight: 300;
    text-transform: uppercase;
    line-height: 1;
  }
  .card--front .brand {
    left: 170px;
    top: 108px;
    color: var(--reverse);
  }
  .brand__name {
    display: block;
    font-size: 44px;
    letter-spacing: 1px;
  }
  .brand__sub {
    display: block;
    font-size: 20px;
    letter-spacing: 1px;
    margin-top: 6px;
    padding-left: 10px;
  }
  .card--back .brand {
    left: 22px;
    top: 58px;
    color: var(--ink);
  }
  .card--back .brand__name { font-size: 27px; }
  .card--back .brand__sub { font-size: 13px; margin-top: 3px; padding-left: 6px; }
  .divider {
    position: absolute;
    left: 153px;
    top: 60px;
    width: 3px;
    height: 240px;
    background: var(--ink);
  }
  .contact {
    position: absolute;
    left: 178px;
    top: 190px;
    list-style: none;
    color: var(--ink);
    text-transform: uppercase;
    font-size: 14px;
    font-weight: 300;
    line-height: 18px;
    letter-spacing: 0.3px;
  }
  .contact strong { font-weight: 600; }
  .contact .small { font-size: 11px; }
</style>
</head>
<body>
  <main class="canvas">
    <section class="card card--front" aria-label="Card front">
      <div class="brand">
        <span class="brand__name">Liora</span>
        <span class="brand__sub">Interiors</span>
      </div>
    </section>

    <section class="card card--back" aria-label="Card back">
      <div class="brand">
        <span class="brand__name">Liora</span>
        <span class="brand__sub">Interiors</span>
      </div>
      <div class="divider"></div>
      <ul class="contact">
        <li><strong>Mirelle Voss Harlan</strong></li>
        <li>(<strong>Dip.</strong> Interior Design)</li>
        <li><strong>Director</strong></li>
        <li><strong>Mob</strong>: 0400555018</li>
        <li><strong>Email</strong>: <span class="small">mirelle@liorainteriors.com.au</span></li>
        <li><strong>Web</strong>: www.liorainteriors.com</li>
      </ul>
    </section>
  </main>
</body>
</html>
```